Expedition Cruise Sales Website for the Polar Regions (Antarctica & Arctic)

This will be a website for selling cruises.
This site should have a homepage, a ship page, destinations, and itineraries.
I have created a file specifying each page, and it is attached.
Pages:
1. Home
2. Cruise Lines
- 2.1 Ships
3. Destinations
- 3.1 Region - 3.2 Country - 3.3 City
4. Itineraries
- 4.1 Itinerary
5. Blog / Travel Tips 6. About Us
7. Contact
Please take a look on the attached pdf
Target Market(s)
Expedition Travelers
Coding
Coded - Design and coding required
Number of Pages Required
5+ page

```html
<!DOCTYPE html>
<html lang="en">
<head>
<meta charset="utf-8">
<title>Polarine — Expedition Cruises</title>
<link href="https://fonts.googleapis.com/css2?family=Outfit:wght@400;500;600;700;800&family=Inter:wght@400;500;600&display=swap" rel="stylesheet">
<style>
:root{
  --navy:#0e1a33;
  --navy-2:#16264a;
  --blue:#1877f2;
  --blue-2:#2f8cff;
  --ink:#111827;
  --muted:#5b6475;
  --light:#eef2f7;
  --white:#ffffff;
  --star:#19b36b;
}
*{box-sizing:border-box;margin:0;padding:0}
html,body{width:1200px;height:4860px;overflow:hidden}
body{position:relative;background:var(--white);font-family:"Inter",sans-serif;color:var(--ink)}
.abs{position:absolute}
h1,h2,h3,h4,.display{font-family:"Outfit",sans-serif}
.btn{display:inline-flex;align-items:center;gap:10px;border-radius:999px;font:600 14px "Inter",sans-serif;color:var(--white);background:var(--navy);padding:12px 24px;text-decoration:none}
.btn-arrow{width:24px;height:24px;border-radius:50%;background:var(--blue);display:inline-flex;align-items:center;justify-content:center}
.photo{position:absolute}

/* Header / hero */
.hero{position:absolute;left:0;top:0;width:1200px;height:720px;background:linear-gradient(180deg,#5e8fb2 0%,#7aa6c4 30%,#3f6f8c 55%,#1e5470 75%,#163e56 100%)}
.nav{position:absolute;left:0;top:0;width:1200px;height:96px;display:flex;align-items:center;padding:0 96px}
.brand{display:flex;align-items:center;gap:10px;font:700 26px "Outfit",sans-serif;color:var(--white)}
.brand-dot{width:14px;height:14px;border-radius:50%;background:var(--white)}
.nav-links{margin-left:auto;display:flex;gap:26px;align-items:center;list-style:none}
.nav-links li{font:500 14px "Inter",sans-serif;color:var(--white)}
.nav-links .active{border-bottom:2px solid var(--white);padding-bottom:4px}
.nav-cta{background:var(--blue);padding:11px 24px;border-radius:999px}
.hero-title{position:absolute;top:76px;left:0;width:1200px;text-align:center;color:var(--white)}
.hero-title .lead{font:500 44px/1.05 "Outfit",sans-serif}
.hero-title .main{font:700 60px/1.05 "Outfit",sans-serif;margin-top:2px}
.hero-sub{position:absolute;top:200px;left:0;width:1200px;text-align:center;color:var(--white);font:400 17px/1.4 "Inter",sans-serif}
.search{position:absolute;left:360px;top:334px;width:470px;height:52px;background:var(--white);border-radius:999px;display:flex;align-items:center;padding:0 6px 0 22px;font-size:14px;color:#8a93a3}
.search .btn{margin-left:auto;padding:11px 22px}

/* Section heads */
.section-head{position:absolute;left:0;width:1200px;text-align:center}
.section-head .eyebrow{font:500 28px "Outfit",sans-serif;color:var(--ink)}
.section-head h2{font:700 50px/1.1 "Outfit",sans-serif;color:var(--ink)}
.section-head p{font:400 15px "Inter",sans-serif;color:var(--muted);margin-top:8px}

/* Offers */
.offer{position:absolute;top:920px;width:316px}
.offer .photo{position:relative;height:300px;border-radius:4px}
.offer h3{font:700 21px "Outfit",sans-serif;text-align:center;margin-top:22px}
.offer p{font:400 13px/1.5 "Inter",sans-serif;color:var(--muted);text-align:center;margin-top:8px;padding:0 14px}
.fav{position:absolute;right:10px;top:10px;width:26px;height:26px;border-radius:4px;background:var(--blue)}
.round-arrow{position:absolute;width:34px;height:34px;border-radius:50%;display:flex;align-items:center;justify-content:center}

/* Destinations */
.dest-copy{position:absolute;width:300px}
.dest-copy h3{font:700 22px "Outfit",sans-serif}
.dest-copy p{font:400 14px/1.55 "Inter",sans-serif;color:var(--muted);margin:10px 0 18px}

/* Cruise lines */
.lines{position:absolute;left:0;top:3300px;width:1200px;height:590px;background:linear-gradient(180deg,#2a3b5c 0%,#3c4f70 45%,#55657f 100%)}
.lines .eyebrow{position:absolute;left:112px;top:44px;font:500 28px "Outfit",sans-serif;color:var(--white)}
.lines h2{position:absolute;left:112px;top:84px;font:700 48px "Outfit",sans-serif;color:var(--white)}
.feature{position:absolute;left:112px;width:460px;color:var(--white)}
.feature h4{font:600 18px "Outfit",sans-serif;display:flex;align-items:center;gap:14px}
.feature p{font:400 13px "Inter",sans-serif;opacity:.85;margin:2px 0 0 50px}
.feature-icon{width:36px;height:36px;border-radius:50%;border:2px solid var(--white)}

/* Reviews */
.reviews{position:absolute;left:0;top:3890px;width:1200px;height:590px;background:var(--light)}
.review{position:absolute;top:4140px;width:292px;height:160px;background:var(--white);border-radius:6px;padding:18px 20px;box-shadow:0 4px 14px rgba(15,25,50,.08)}
.stars{display:flex;gap:3px;align-items:center}
.star{width:16px;height:16px;background:var(--star)}
.verified{font:500 11px "Inter",sans-serif;color:var(--muted);margin-left:8px}
.review h4{font:600 15px "Outfit",sans-serif;margin-top:12px}
.review p{font:400 12px/1.5 "Inter",sans-serif;color:var(--muted);margin-top:4px}
.review .who{font:500 11px "Inter",sans-serif;color:var(--ink);margin-top:10px}

/* CTA */
.cta{position:absolute;left:112px;top:4330px;width:976px;height:260px;background:linear-gradient(90deg,#1168e0,#2f8cff);text-align:center;color:var(--white);padding-top:44px;z-index:2}
.cta h2{font:700 52px "Outfit",sans-serif}
.cta p{font:400 15px/1.5 "Inter",sans-serif;margin-top:10px}
.cta .btn{margin-top:20px;padding:10px 22px}
.cta small{display:block;margin-top:14px;font-size:12px;opacity:.85}

/* Footer */
.footer{position:absolute;left:0;top:4480px;width:1200px;height:380px;background:var(--navy)}
.footer .brand{position:absolute;left:112px;top:190px;font-size:34px}
.foot-col{position:absolute;top:160px;color:var(--white);width:300px}
.foot-col h4{font:600 18px "Outfit",sans-serif}
.foot-col p{font:400 12px/1.5 "Inter",sans-serif;opacity:.75;margin-top:6px}
.foot-col .btn{background:var(--blue);padding:8px 18px;font-size:12px;margin-top:12px}
.subscribe{position:absolute;left:760px;top:244px;width:330px;height:40px;background:var(--white);border-radius:999px;display:flex;align-items:center;padding:0 4px 0 16px;font-size:12px;color:#8a93a3}
.subscribe span.btn{margin-left:auto;background:var(--blue);padding:8px 16px;font-size:12px}
.socials{position:absolute;right:112px;top:300px;display:flex;gap:10px}
.socials i{width:26px;height:26px;border-radius:50%;background:var(--blue);display:block}
.foot-rule{position:absolute;left:112px;top:334px;width:976px;height:1px;background:rgba(255,255,255,.15)}
.foot-links{position:absolute;left:112px;top:346px;display:flex;gap:28px;list-style:none;font:400 13px "Inter",sans-serif;color:var(--white)}
</style>
</head>
<body>

<!-- Hero -->
<header class="hero">
  <div class="photo" role="img" aria-label="White ferry cruising fast over blue water with a city skyline behind" style="left:0;top:0;width:1200px;height:720px;background:linear-gradient(180deg,rgba(40,70,100,.55) 0%,rgba(120,160,190,0) 35%,rgba(20,60,85,.3) 100%)"></div>
  <nav class="nav">
    <div class="brand"><span class="brand-dot"></span>Polarine</div>
    <ul class="nav-links">
      <li class="active">Home</li>
      <li>Cruise Lines ▾</li>
      <li>Destinations ▾</li>
      <li>Itineraries ▾</li>
      <li>Blog / Travel Tips</li>
      <li>About</li>
      <li class="nav-cta">Contact</li>
    </ul>
  </nav>
  <div class="hero-title">
    <div class="lead">Set Sail on the</div>
    <h1 class="main">Adventure of a Lifetime</h1>
  </div>
  <p class="hero-sub">Explore breathtaking destinations, luxury cruises, and exclusive deals — only with Polarine.</p>
  <div class="search">Search cruises...<span class="btn">Search Now</span></div>
</header>

<!-- Featured offers -->
<div class="section-head" style="top:784px">
  <div class="eyebrow">Limited-Time Deals</div>
  <h2>Featured Offers</h2>
  <p>Find the perfect cruise at unbeatable prices.</p>
</div>
<div class="round-arrow" style="left:62px;top:1054px;background:var(--navy)"><svg width="12" height="12" viewBox="0 0 12 12"><path d="M8 2 4 6l4 4" stroke="#fff" stroke-width="2" fill="none"/></svg></div>
<div class="round-arrow" style="left:1104px;top:1054px;background:var(--blue)"><svg width="12" height="12" viewBox="0 0 12 12"><path d="M4 2l4 4-4 4" stroke="#fff" stroke-width="2" fill="none"/></svg></div>

<article class="offer" style="left:112px">
  <div class="photo" role="img" aria-label="Cruise ship among snowy Antarctic mountains" style="background:linear-gradient(180deg,#9fb4c6 0%,#6c8194 45%,#2f4457 100%)"><span class="fav"></span></div>
  <h3>Best Antarctic Cruises</h3>
  <p>Sail through our iconic landscapes, spot majestic wildlife, and experience the wonders of the polar region.</p>
</article>
<article class="offer" style="left:442px">
  <div class="photo" role="img" aria-label="Aerial view of boats in a turquoise island bay" style="background:linear-gradient(160deg,#1aa3b5 0%,#2fc0c4 40%,#157d96 100%)"><span class="fav"></span></div>
  <h3>Top Galápagos Cruises</h3>
  <p>Witness rare wildlife, crystal-clear waters, and guided excursions in one of the world's unique destinations.</p>
</article>
<article class="offer" style="left:772px">
  <div class="photo" role="img" aria-label="Couple relaxing on a sunny cruise deck" style="background:linear-gradient(180deg,#cfe0ea 0%,#d9c2a6 55%,#8d6e55 100%)"><span class="fav"></span></div>
  <h3>Last-Minute Cruise Deals</h3>
  <p>Ready for a spontaneous adventure? Get up to 30% off select cruises—book before they're gone.</p>
</article>
<div class="abs" style="left:0;top:1370px;width:1200px;text-align:center"><span class="btn">View All Offers</span></div>

<!-- Destinations -->
<div class="section-head" style="top:1472px">
  <div class="eyebrow">Explore Our</div>
  <h2>Highlighted Destinations</h2>
  <p>Where will your next journey take you?</p>
</div>

<div class="photo" role="img" aria-label="Palm trees over a tropical resort pool and sea" style="left:0;top:1628px;width:740px;height:472px;background:linear-gradient(180deg,#cfe6f4 0%,#7fb0d1 30%,#3b7f3f 55%,#2aa6b4 80%,#1b7e93 100%)"></div>
<div class="dest-copy" style="left:772px;top:1782px">
  <h3>Caribbean Paradise</h3>
  <p>Relax on white-sand beaches, explore tropical islands, and enjoy crystal-clear waters.</p>
  <span class="btn">Learn More <span class="btn-arrow"><svg width="10" height="10" viewBox="0 0 10 10"><path d="M3 1l4 4-4 4" stroke="#fff" stroke-width="1.8" fill="none"/></svg></span></span>
</div>

<div class="photo" role="img" aria-label="Yachts moored in a Mediterranean harbour below a hillside town" style="left:460px;top:2152px;width:740px;height:468px;background:linear-gradient(180deg,#6fa6dc 0%,#a9cbe8 35%,#c9b79a 55%,#e9eef2 75%,#3d6b8c 100%)"></div>
<div class="dest-copy" style="left:120px;top:2302px">
  <h3>Mediterranean Wonders</h3>
  <p>Cruise through historic cities, stunning coastlines, and enjoy world-class cuisine.</p>
  <span class="btn">Learn More <span class="btn-arrow"><svg width="10" height="10" viewBox="0 0 10 10"><path d="M3 1l4 4-4 4" stroke="#fff" stroke-width="1.8" fill="none"/></svg></span></span>
</div>

<div class="photo" role="img" aria-label="Snow-capped glacier mountains above icy blue water" style="left:0;top:2672px;width:740px;height:480px;background:linear-gradient(180deg,#2f7fd0 0%,#7bb4e6 35%,#e8f1f8 55%,#6f8fa9 70%,#2a6d9a 100%)"></div>
<div class="dest-copy" style="left:772px;top:2822px">
  <h3>Alaskan Glaciers &amp; Wildlife</h3>
  <p>Marvel at towering glaciers, breathtaking fjords, and unforgettable wildlife encounters.</p>
  <span class="btn">Learn More <span class="btn-arrow"><svg width="10" height="10" viewBox="0 0 10 10"><path d="M3 1l4 4-4 4" stroke="#fff" stroke-width="1.8" fill="none"/></svg></span></span>
</div>
<div class="abs" style="left:0;top:3186px;width:1200px;text-align:center"><span class="btn">Discover More Destinations</span></div>

<!-- Cruise line highlights -->
<section class="lines">
  <div class="photo" role="img" aria-label="Cruise ship sailing under dramatic clouds" style="left:0;top:0;width:1200px;height:590px;background:linear-gradient(180deg,rgba(20,30,50,.4),rgba(140,150,165,.25))"></div>
  <div class="eyebrow">Travel with the Best</div>
  <h2>Cruise Line Highlights</h2>
  <div class="feature" style="top:190px"><h4><span class="feature-icon"></span>Luxury Voyages</h4><p>5-star service, gourmet dining, and suite-class accommodations.</p></div>
  <div class="feature" style="top:270px"><h4><span class="feature-icon"></span>Adventure Cruises</h4><p>Exciting expeditions to the world's most remote destinations.</p></div>
  <div class="feature" style="top:350px"><h4><span class="feature-icon"></span>Family-Friendly Cruises</h4><p>Onboard entertainment for all ages, activities, and kid-friendly cuisine.</p></div>
  <span class="btn abs" style="left:112px;top:430px;background:var(--navy)">See All Cruise Lines</span>
  <div class="photo" role="img" aria-label="Large cruise ship at sea" style="left:112px;top:490px;width:360px;height:80px;background:linear-gradient(180deg,#c9d2dc,#5d6f86)"></div>
  <div class="photo" role="img" aria-label="Cruise ship pool deck from above" style="left:700px;top:230px;width:230px;height:260px;background:linear-gradient(160deg,#3a8fbf,#c8a98b 60%,#8b6a4f);border:4px solid #fff"></div>
  <div class="photo" role="img" aria-label="Tall cruise ship decks against a blue sky" style="left:930px;top:80px;width:210px;height:260px;background:linear-gradient(180deg,#6fa7dd,#e7eef5 60%,#8aa3bb);border:4px solid #fff"></div>
  <div class="photo" role="img" aria-label="Family enjoying a water slide on deck" style="left:930px;top:340px;width:210px;height:220px;background:linear-gradient(180deg,#4aa3e0,#e6b04a 55%,#d9573a);border:4px solid #fff"></div>
</section>

<!-- Reviews -->
<section class="reviews"></section>
<div class="section-head" style="top:3984px">
  <div class="eyebrow">Real Customer Reviews</div>
  <h2>What Our Travelers Say</h2>
</div>
<div class="round-arrow" style="left:104px;top:4202px;background:var(--navy)"><svg width="12" height="12" viewBox="0 0 12 12"><path d="M8 2 4 6l4 4" stroke="#fff" stroke-width="2" fill="none"/></svg></div>
<div class="round-arrow" style="left:1060px;top:4202px;background:var(--blue)"><svg width="12" height="12" viewBox="0 0 12 12"><path d="M4 2l4 4-4 4" stroke="#fff" stroke-width="2" fill="none"/></svg></div>

<div class="review" style="left:152px">
  <div class="stars"><i class="star"></i><i class="star"></i><i class="star"></i><i class="star"></i><i class="star"></i><span class="verified">Verified</span></div>
  <h4>An unforgettable experience!</h4>
  <p>The ship was stunning and every excursion felt perfectly planned.</p>
  <div class="who">Emma R. · 2 days ago</div>
</div>
<div class="review" style="left:454px">
  <div class="stars"><i class="star"></i><i class="star"></i><i class="star"></i><i class="star"></i><i class="star"></i><span class="verified">Verified</span></div>
  <h4>Our family had the best vacation</h4>
  <p>Kids loved the activities and we loved the calm polar views.</p>
  <div class="who">Daniel K. · 1 week ago</div>
</div>
<div class="review" style="left:756px">
  <div class="stars"><i class="star"></i><i class="star"></i><i class="star"></i><i class="star"></i><i class="star"></i><span class="verified">Verified</span></div>
  <h4>I booked a last-minute deal</h4>
  <p>Great price, friendly crew, and an itinerary worth every penny.</p>
  <div class="who">Sofia M. · 3 weeks ago</div>
</div>

<!-- CTA -->
<section class="cta">
  <h2>Ready to Set Sail</h2>
  <p>Your perfect cruise is waiting. Explore, book, and get ready for<br>an adventure of a lifetime.</p>
  <span class="btn">Find Your Cruise Now</span>
  <small>Questions? Talk to a cruise expert today.</small>
</section>

<!-- Footer -->
<footer class="footer">
  <div class="brand"><span class="brand-dot"></span>Polarine</div>
  <div class="foot-col" style="left:420px">
    <h4>Join Our ChatLine List</h4>
    <p>Get exclusive deals and cruise updates<br>straight to your phone.</p>
    <span class="btn">Join Now</span>
  </div>
  <div class="foot-col" style="left:760px">
    <h4>Join Our Cruise Community</h4>
    <p>Be the first to know about new cruise deals,<br>exclusive promotions, and travel tips.</p>
  </div>
  <div class="subscribe">Enter your email<span class="btn">Subscribe Now</span></div>
  <div class="socials"><i></i><i></i><i></i></div>
  <div class="foot-rule"></div>
  <ul class="foot-links">
    <li>Home</li><li>Cruise Lines</li><li>Destinations</li><li>Itineraries</li><li>Blog</li><li>Travel Tips</li><li>About</li><li>Contact</li>
  </ul>
</footer>

</body>
</html>
```